website for 'thebrightnook' which is a specialise tutoring company for children with learning difficu

We need a website for a new business that is focused on assessment and then specialised tutoring for young children with learning difficulties. The website needs to be simple but fun and fresh. We have an existing logo (uploaded) that needs to be the building block for the website. The website doesn't need to be overly content-heavy.

Target Market(s)

parents

Industry/Entity Type

Education

Number of Pages Required

3 page

Font styles to use
Other font styles liked:
• possibly matched to the logo

Requirements
Must have
• a initial front page which introduces the business and provides contact details, a second page that will allow for a more content-heavy section, a third page which focuses on introducing the staff (initially 3 staff ),

```html
<!DOCTYPE html>
<html lang="en">
<head>
<meta charset="utf-8">
<title>thebrightnook – specialised learning for children</title>
<link href="https://fonts.googleapis.com/css2?family=Gabriela&family=Fredoka:wght@300;400;700&family=Open+Sans:wght@400&display=swap" rel="stylesheet">
<style>
:root{
  --green:#8dc63f;
  --green-dark:#5e9a22;
  --navy:#063f7e;
  --pink:#fa5a74;
  --yellow:#f8b51b;
  --ink:#2b2b2b;
  --grey:#6f6f6f;
  --white:#ffffff;
  --rule:#e3e3e3;
}
*{margin:0;padding:0;box-sizing:border-box}
html,body{width:1200px;height:1172px;overflow:hidden;background:var(--white)}
body{position:relative;font-family:"Gabriela",serif;color:var(--ink)}

/* header */
.site-header{position:absolute;left:0;top:0;width:1200px;height:115px;background:var(--white)}
.brand{position:absolute;left:85px;top:50px;display:flex;align-items:center;gap:8px}
.brand-dot{width:13px;height:13px;border-radius:50%;background:var(--green)}
.brand-name{font-family:"Gabriela",serif;font-size:24px;color:var(--green-dark);line-height:1}
.brand-tag{position:absolute;left:85px;top:87px;font-size:7.5px;letter-spacing:1.2px;color:var(--grey)}
.nav{position:absolute;top:41px;left:580px;width:380px;height:33px;font-family:"Gabriela",serif;font-size:14px;color:#444}
.nav a{color:inherit;text-decoration:none;position:absolute;white-space:nowrap}
.nav .home{left:0;top:0;width:71px;height:33px;background:var(--green);color:var(--white);display:flex;align-items:center;justify-content:center;border-radius:2px}
.nav .item{top:8px}
.header-phone{position:absolute;left:986px;top:48px;display:flex;align-items:center;gap:8px;font-family:"Fredoka",sans-serif;font-weight:700;font-size:15.5px;color:var(--pink)}

/* hero */
.hero{position:absolute;left:0;top:115px;width:1200px;height:533px;background:var(--navy)}
.hero-title{position:absolute;left:84px;top:164px;font-family:"Fredoka",sans-serif;font-weight:700;font-size:40px;color:var(--white);letter-spacing:.5px;white-space:nowrap}
.hero-sub{position:absolute;left:84px;top:215px;font-family:"Open Sans",sans-serif;font-size:24px;color:var(--yellow);white-space:nowrap}
.hero-text{position:absolute;left:85px;top:256px;width:290px;font-size:13.5px;line-height:19.5px;color:var(--white)}
.hero-btn{position:absolute;left:86px;top:344px;width:184px;height:41px;border:1.5px solid var(--white);border-radius:21px;display:flex;align-items:center;justify-content:center;font-family:"Fredoka",sans-serif;font-size:16px;color:var(--white)}
.hero-photo{position:absolute;left:737px;top:78px;width:387px;height:455px;border-radius:190px 190px 0 0;background:linear-gradient(160deg,#6b4a35 0%,#e8c4b0 35%,#1f2f5c 65%,#17244a 100%)}

/* welcome */
.welcome{position:absolute;left:0;top:648px;width:1200px;height:290px}
.welcome h1{position:absolute;left:85px;top:56px;font-weight:400;font-size:28px;color:var(--grey);white-space:nowrap}
.welcome h1 span{color:var(--green-dark)}
.lead{position:absolute;left:85px;top:108px;font-size:14.5px;line-height:24px;color:var(--ink)}
.body-copy{position:absolute;left:85px;top:172px;width:720px;font-size:13.5px;line-height:23px;color:#3a3a3a}
.side-rule{position:absolute;left:1111px;top:0;width:1px;height:290px;background:var(--rule)}
.about-tab{position:absolute;left:918px;top:93px;width:194px;height:47px;background:var(--pink);border-radius:24px 0 0 0;display:flex;align-items:center;justify-content:center;font-family:"Gabriela",serif;font-size:16px;color:var(--white)}
.bird{position:absolute;left:940px;top:60px;width:32px;height:32px;border-radius:50%;background:var(--yellow)}

/* footer */
.site-footer{position:absolute;left:0;top:938px;width:1200px;height:234px;background:var(--green);overflow:hidden}
.footer-brand{position:absolute;left:87px;top:122px;display:flex;align-items:center;gap:8px}
.footer-brand .brand-dot{background:var(--white)}
.footer-brand .brand-name{color:var(--white)}
.footer-tag{position:absolute;left:87px;top:155px;font-size:7.5px;letter-spacing:1.2px;color:var(--white)}
.copyright{position:absolute;left:87px;top:173px;font-size:8.5px;color:var(--white)}
.contact-title{position:absolute;left:591px;top:98px;font-size:29px;color:var(--white);white-space:nowrap}
.footer-phone{position:absolute;left:818px;top:56px;display:flex;align-items:center;gap:10px;font-family:"Fredoka",sans-serif;font-weight:300;font-size:27px;letter-spacing:1px;color:var(--white)}
.footer-mail{position:absolute;left:818px;top:95px;width:185px;padding-bottom:6px;border-bottom:1px solid rgba(255,255,255,.6);display:flex;align-items:center;gap:9px;font-size:13.5px;color:var(--white);white-space:nowrap}
.footer-address{position:absolute;left:819px;top:138px;font-size:13.5px;line-height:16px;color:var(--white)}
.social{position:absolute;left:1012px;top:189px;display:flex;gap:14px}
.social span{width:14px;height:14px;border-radius:50%;background:var(--white)}
</style>
</head>
<body>

<header class="site-header">
  <div class="brand"><span class="brand-dot"></span><span class="brand-name">thebrightnook</span></div>
  <div class="brand-tag">specialised learning for children</div>
  <nav class="nav">
    <a class="home" href="#">Home</a>
    <a class="item" style="left:90px" href="#">Who we are</a>
    <a class="item" style="left:205px" href="#">Our team</a>
    <a class="item" style="left:301px" href="#">Contact us</a>
  </nav>
  <div class="header-phone">
    <svg width="13" height="13" viewBox="0 0 24 24"><path fill="#9a9a9a" d="M6.6 10.8c1.4 2.8 3.8 5.1 6.6 6.6l2.2-2.2c.3-.3.7-.4 1-.2 1.1.4 2.3.6 3.6.6.6 0 1 .4 1 1V20c0 .6-.4 1-1 1C10.6 21 3 13.4 3 4c0-.6.4-1 1-1h3.5c.6 0 1 .4 1 1 0 1.3.2 2.5.6 3.6.1.3 0 .7-.2 1z"/></svg>
    <span>0412 558 306</span>
  </div>
</header>

<section class="hero">
  <h2 class="hero-title">Lorem ipsum dolor sit</h2>
  <p class="hero-sub">consectetuer adipiscing elit.</p>
  <p class="hero-text">Lorem ipsum dolor sit amet, consectetuer adipiscing elit. Aenean commodo ligula eget dolor</p>
  <a class="hero-btn">See info</a>
  <div class="hero-photo" role="img" aria-label="Photo of a young girl in a navy polka-dot vest blowing soap bubbles"></div>
</section>

<section class="welcome">
  <h1>Wellcom to <span>The Bright Nook</span></h1>
  <p class="lead">Lorem ipsum dolor sit amet, consectetuer adipiscing elit.<br>Aenean commodo ligula eget dolor.</p>
  <p class="body-copy">Lorem ipsum dolor sit amet, consectetuer adipiscing elit. Aenean commodo ligula eget dolor. Aenean massa. Cum sociis natoque penatibus et magnis dis parturient montes, nascetur ridiculus mus. Donec quam felis, ultricies nec, pellentesque eu, pretium quis, sem. Nulla consequat massa quis enim.</p>
  <div class="side-rule"></div>
  <div class="bird" role="img" aria-label="Illustration of a small yellow bird perched on the tab"></div>
  <div class="about-tab">About Us</div>
</section>

<footer class="site-footer">
  <div class="footer-brand"><span class="brand-dot"></span><span class="brand-name">thebrightnook</span></div>
  <div class="footer-tag">specialised learning for children</div>
  <div class="copyright">Copyright © thebrightnook.com 2016</div>

  <div class="contact-title">Contact us</div>

  <div class="footer-phone">
    <svg width="17" height="17" viewBox="0 0 24 24"><path fill="#ffffff" d="M6.6 10.8c1.4 2.8 3.8 5.1 6.6 6.6l2.2-2.2c.3-.3.7-.4 1-.2 1.1.4 2.3.6 3.6.6.6 0 1 .4 1 1V20c0 .6-.4 1-1 1C10.6 21 3 13.4 3 4c0-.6.4-1 1-1h3.5c.6 0 1 .4 1 1 0 1.3.2 2.5.6 3.6.1.3 0 .7-.2 1z"/></svg>
    <span>0412 558 306</span>
  </div>
  <div class="footer-mail">
    <svg width="13" height="10" viewBox="0 0 13 10"><rect width="13" height="10" rx="1" fill="#ffffff"/><path d="M1 1 L6.5 5.5 L12 1" fill="none" stroke="#8dc63f" stroke-width="1.2"/></svg>
    <span>info@thebrightnook.com</span>
  </div>
  <p class="footer-address">Nora J. Whitfield 2240<br>Maple Grove Lane,<br>OR 97204</p>

  <div class="social" aria-label="Social links">
    <span></span><span></span><span></span>
  </div>
</footer>

</body>
</html>
```